Robotic Physical Therapy office needs a Grand Opening Flyer

We need a Grand Opening flyer design for a robotic physical therapy office named Stellar Motion Therapy. We would like it to have a clean, classy, upscale feeling that gives potential clients a V.I.P. feeling. We would like to use the colors black, gray, and yellow (logo will be uploaded).

Event: Thursday, June 1st, 2023 from 12pm-6pm
location: 58274 Harlow Ave, Bloomfield Hills, MI 48319

Industry/Entity Type

Physical therapy

Font styles to use
Script

Colors

Designer to choose colors to be used in the design.

Requirements
Nice to have
• More of a vip feel for the invite

```html
<!DOCTYPE html>
<html lang="en">
<head>
<meta charset="utf-8">
<title>Stellar Motion Therapy — Grand Opening</title>
<link rel="stylesheet" href="https://fonts.googleapis.com/css2?family=Abril+Fatface&family=Bodoni+Moda:opsz,wght@6..96,400;6..96,500&display=swap">
<style>
  :root {
    --ink-deep: #0f100f;
    --ink-mid: #232422;
    --gold-dark: #c8952e;
    --gold: #e0a93c;
    --gold-light: #fbd27a;
    --brand-yellow: #f4da2c;
    --paper: #ffffff;
  }
  * { margin: 0; padding: 0; box-sizing: border-box; }
  html, body { width: 848px; height: 1200px; overflow: hidden; background: var(--ink-deep); }
  .flyer {
    position: relative;
    width: 848px;
    height: 1200px;
    overflow: hidden;
    background: radial-gradient(ellipse 60% 50% at 50% 52%, var(--ink-mid) 0%, #191a19 55%, var(--ink-deep) 100%);
    font-family: "Bodoni Moda", "Times New Roman", serif;
    color: var(--paper);
  }
  .frame {
    position: absolute;
    left: 30px; top: 33px;
    width: 788px; height: 1132px;
    border: 2px solid var(--gold);
  }
  .gold-glow {
    position: absolute;
    pointer-events: none;
    background: radial-gradient(ellipse at center, rgba(224,169,60,.45), rgba(224,169,60,0) 70%);
  }
  .glow-top-left { left: 0; top: 60px; width: 130px; height: 130px; }
  .glow-top { left: 380px; top: 0; width: 120px; height: 70px; }
  .glow-right-upper { left: 740px; top: 270px; width: 108px; height: 150px; }
  .glow-right-lower { left: 730px; top: 660px; width: 118px; height: 180px; }
  .glow-bottom-left { left: 60px; top: 1110px; width: 200px; height: 90px; }
  .glow-ribbon {
    left: 330px; top: 858px; width: 518px; height: 342px;
    background:
      radial-gradient(ellipse 22% 60% at 88% 40%, rgba(240,180,70,.5), transparent 70%),
      radial-gradient(ellipse 60% 22% at 50% 90%, rgba(230,170,60,.55), transparent 70%);
  }
  .glow-sparkles {
    left: 180px; top: 260px; width: 490px; height: 330px;
    background: radial-gradient(ellipse at center, rgba(251,210,122,.07), rgba(251,210,122,0) 70%);
  }
  .bokeh {
    position: absolute;
    left: 90px; top: 920px;
    width: 680px; height: 280px;
    background: radial-gradient(ellipse at 50% 60%, rgba(120,120,110,.18), transparent 70%);
  }
  .brand {
    position: absolute;
    left: 0; right: 0; top: 112px;
    display: flex; justify-content: center; align-items: center; gap: 14px;
  }
  .brand-dot {
    width: 58px; height: 58px;
    border-radius: 50%;
    border: 4px solid var(--paper);
  }
  .brand-name {
    font-weight: 500;
    font-size: 34px;
    line-height: 1.05;
    color: var(--brand-yellow);
    letter-spacing: .5px;
    text-transform: uppercase;
  }
  .title { position: absolute; left: 0; top: 0; }
  .ornament {
    position: absolute;
    left: 379px; width: 90px; height: 30px;
    background: radial-gradient(ellipse at center, rgba(255,255,255,.35), rgba(255,255,255,0) 70%);
  }
  .ornament.upper { top: 652px; }
  .ornament.lower { top: 931px; }
  .event-date {
    position: absolute;
    left: 150px; top: 713px; width: 548px;
    display: flex; justify-content: space-between; align-items: center;
    font-size: 35px; letter-spacing: 1px;
    color: var(--paper);
  }
  .event-date .sep { font-size: 38px; color: var(--paper); }
  .event-time {
    position: absolute; left: 0; right: 0; top: 785px;
    text-align: center; font-size: 29px; word-spacing: 6px;
  }
  .event-address {
    position: absolute; left: 0; right: 0; top: 856px;
    text-align: center; font-size: 21.5px; letter-spacing: .2px;
  }
</style>
</head>
<body>
<main class="flyer">
  <div class="gold-glow glow-top-left" role="img" aria-label="Blurred gold confetti"></div>
  <div class="gold-glow glow-top" role="img" aria-label="Blurred gold confetti"></div>
  <div class="gold-glow glow-right-upper" role="img" aria-label="Blurred gold confetti"></div>
  <div class="gold-glow glow-right-lower" role="img" aria-label="Blurred gold confetti"></div>
  <div class="gold-glow glow-bottom-left" role="img" aria-label="Blurred gold confetti"></div>
  <div class="bokeh" role="img" aria-label="Soft glowing bokeh lights"></div>
  <div class="frame"></div>
  <div class="gold-glow glow-ribbon" role="img" aria-label="Curling gold satin ribbon"></div>
  <div class="gold-glow glow-sparkles" role="img" aria-label="Small gold sparkle stars around the headline"></div>

  <header class="brand">
    <span class="brand-dot"></span>
    <span class="brand-name">Stellar Motion<br>Therapy</span>
  </header>

  <svg class="title" width="848" height="1200" viewBox="0 0 848 1200">
    <defs>
      <linearGradient id="goldFoil" x1="0" y1="0" x2="1" y2="0">
        <stop offset="0" stop-color="#c8952e"/>
        <stop offset=".35" stop-color="#fbd27a"/>
        <stop offset=".6" stop-color="#d9a23a"/>
        <stop offset="1" stop-color="#fbd27a"/>
      </linearGradient>
    </defs>
    <text x="434" y="405" text-anchor="middle" textLength="284" lengthAdjust="spacing"
          font-family="'Bodoni Moda', serif" font-size="74" fill="url(#goldFoil)">GRAND</text>
    <text x="424" y="522" text-anchor="middle" textLength="470" lengthAdjust="spacingAndGlyphs"
          font-family="'Abril Fatface', serif" font-size="112" fill="url(#goldFoil)">OPENING</text>
  </svg>

  <div class="ornament upper" role="img" aria-label="White calligraphic flourish divider"></div>

  <p class="event-date">
    <span>THURSDAY</span><span class="sep">|</span><span>1st&nbsp; JUNE</span><span class="sep">|</span><span>2023</span>
  </p>
  <p class="event-time">12:00 pm &nbsp; - &nbsp; 6:00 pm</p>
  <p class="event-address">58274 Harlow Ave, Bloomfield Hills, MI 48319</p>

  <div class="ornament lower" role="img" aria-label="White calligraphic flourish divider"></div>
</main>
</body>
</html>
```